New UI for electricity data tool

We are looking for a new UI for the website http://voltmeadow.net. Reassessing the structure of the website is as important as specific design choices. We have created a uniquely comprehensive set of global electricity generation data and now we are looking for creative solutions for how to make this data accessible. Researching and referencing other similar projects may be a good idea.

Goals:
• The website should clearly communicate the most important general conclusions that can be drawn from the data, including:
◦ The world as a whole is not moving away from fossil fuels for electricity generation
◦ There are substantial differences between regions
▪ Some regions have basically solved the problem – they already generate almost all of their electricity from non-fossil sources
▪ Some regions have greatly improved in terms of decarbonizing their electricity generation.
▪ Some regions have greatly deteriorated, in other words they are using a much higher share of fossil fuels to generate their electricity.
◦ There are substantial differences between energy sources. Regions that have successfully decarbonized their electricity generation have usually done so using hydro and/or nuclear. Other low-carbon energy sources have grown quickly in relative terms in the last few years but are so far contributing little in absolute numbers.
• The website should serve as inspiration for energy policy debates. The goal is to study the impact of existing policies around the world. Energy policy here refers to particular combinations of energy sources – ie how much have the countries invested in each type of electricity generation. The tool should help answer questions such as:
◦ Which countries have done the most in terms of decarbonizing their electricity generation?
◦ Which types of energy polices have lead to the fastest decarbonization processes around the world?
◦ If country A changed its energy policy to be more like country B, what would the likely impact be?

Challenges:
• There is a lot of data – it can be overwhelming to the user. It’s crucial to make the site easy to navigate. The main page should highlight the most important data, and it should also be straightforward to find more detailed data.
• Data availability varies from region to region. The current interface addresses this with the default option “Exclude regions with limited data”. We expect a better approach to dealing with this issue. For some regions and years energy sources are grouped together as for example “other renewables” whereas in other cases more detailed data is available.
• Credibility is crucial. Our data is based on a combination of data from KQ and the Tessaro Fund. It must be very clear throughout the site where each data set comes from.

Details:
• The current chart color schemes is loosely based on the carbon emissions from each energy source. This should not necessarily be so. The goal is to on the one hand communicate clearly the amounts of fossil vs non-fossil energy that are generated by each region. At the same time we also want to make it easy to view specific energy sources.

Inspirational websites:
• https://www.trendlooper.org/
• https://pelmarstatix.org/

Let's simplify. The main metric to focus on is Fernhollow Watt and the extent to which the world and each country has achieved it (eg Iceland 100%, France 88% and so on). I'm considering changing the name of the site to FernhollowWatt.org. We can use maps, charts and perhaps other tools to communicate this main message. What's the best way of doing this?

```html
<!DOCTYPE html>
<html lang="en">
<head>
<meta charset="utf-8">
<title>FernhollowWatt.org – Charts</title>
<link href="https://fonts.googleapis.com/css2?family=Lato:wght@400;700&family=Merriweather:wght@700&display=swap" rel="stylesheet">
<style>
:root{
  --ink:#0d2138;
  --text:#2a3545;
  --muted:#6b7684;
  --green:#27c98f;
  --line:#e4e7eb;
  --panel:#f2f4f6;
  --panel-soft:#f8f9fa;
  --brazil:#1f6fa8;
  --us:#8b22c4;
  --uk:#c4161c;
  --india:#12b3a0;
  --china:#b59a10;
}
*{box-sizing:border-box;margin:0;padding:0}
html,body{width:694px;height:1200px;overflow:hidden;background:#fff}
body{font-family:"Lato",sans-serif;color:var(--ink)}
.page{position:absolute;left:0;top:0;width:1440px;height:2490px;transform:scale(.48194);transform-origin:0 0}
.abs{position:absolute}
.header{left:0;top:0;width:1440px;height:127px;border-bottom:2px solid #eceef0}
.brand{left:55px;top:64px;font-size:23px;font-weight:700}
.nav{top:68px;font-size:19px;font-weight:700}
.nav-active{border-bottom:3px solid var(--green);height:59px;left:976px;top:68px;width:79px;text-align:center}
.vsep{left:1090px;top:55px;width:1px;height:50px;background:var(--line)}
.action{top:67px;font-size:20px;color:var(--green);display:flex;align-items:center;gap:12px}
h1,h2,h3{font-family:"Merriweather",serif;font-weight:700}
h1{left:55px;top:176px;font-size:26px}
.lead{left:55px;top:232px;width:1330px;font-size:15px;line-height:26px;color:var(--text)}
.select{height:36px;border:1px solid #cfd4da;border-radius:3px;display:flex;align-items:center;justify-content:space-between;padding:0 14px;font-size:16px;font-weight:700}
.crumb{top:385px;font-size:16px;font-weight:700}
.crumb a{color:var(--green);font-weight:400;margin-left:14px}
.toggle{left:775px;top:382px;width:48px;height:24px;border-radius:12px;background:var(--ink)}
.toggle::after{content:"";position:absolute;right:3px;top:3px;width:18px;height:18px;border-radius:50%;background:var(--green)}
.hint{left:55px;top:466px;font-size:15px;font-weight:700}
.chart{left:0;top:520px}
.axis{font-size:15px;fill:var(--ink)}
.series-label{font-size:15px}
h2.energy{left:55px;top:1155px;font-size:26px}
.energy-note{left:281px;top:1165px;font-size:15px;font-weight:700}
.src-panel{top:1205px;height:220px;background:var(--panel-soft)}
.opt{position:absolute;display:flex;align-items:center;font-size:16px;font-weight:700}
.radio{width:24px;height:24px;border:1px solid #b9c0c8;border-radius:50%;background:#fff;margin-right:14px;position:relative}
.radio.on::after{content:"";position:absolute;left:8px;top:8px;width:7px;height:7px;border-radius:50%;background:var(--ink)}
.sw{width:19px;height:19px;margin-right:16px;border:1px solid rgba(0,0,0,.08)}
.regions{left:55px;top:1440px;width:1330px;height:406px;background:var(--panel)}
.regions h3{position:absolute;left:45px;top:40px;font-size:26px}
.box{width:24px;height:24px;border:1px solid #b9c0c8;border-radius:3px;background:#fff;margin-right:16px;display:flex;align-items:center;justify-content:center}
.box.on{background:var(--ink);border-color:var(--ink)}
.search{position:absolute;left:877px;top:40px;width:408px;height:36px;border:1px solid #cfd4da;background:#fff;border-radius:3px;font-size:15px;color:#b3bac2;padding:8px 14px}
.grid{position:absolute;left:45px;top:120px}
.cell{position:absolute;display:flex;align-items:center;font-size:16px;font-weight:700;white-space:nowrap}
.scroll{position:absolute;right:0;top:100px;width:14px;height:306px;background:#e1e4e8}
.scroll i{position:absolute;left:4px;top:0;width:7px;height:60px;border-radius:4px;background:var(--ink)}
h2.concl{left:55px;top:1915px;font-size:26px}
.concl-lead{left:55px;top:1970px;width:1330px;font-size:15px;line-height:26px;color:var(--text)}
ul.points{list-style:none;font-size:15px;font-weight:700;line-height:28px;color:var(--ink)}
ul.points li{position:relative;padding-left:18px;margin-bottom:8px}
ul.points li::before{content:"";position:absolute;left:3px;top:12px;width:5px;height:5px;border-radius:50%;background:var(--ink)}
ul.points ul{list-style:none;margin-top:6px}
ul.points ul li::before{border-radius:0;width:4px;height:4px}
.footer{top:2418px;font-size:15px;font-weight:700}
.footer a{color:var(--ink)}
.footer a.mail{color:var(--green)}
</style>
</head>
<body>
<div class="page">
  <header class="header abs">
    <div class="brand abs">FernhollowWatt.org</div>
    <div class="nav abs" style="left:862px">Maps</div>
    <div class="nav nav-active abs">Charts</div>
    <div class="vsep abs"></div>
    <div class="action abs" style="left:1135px">
      <svg width="22" height="20" viewBox="0 0 22 20" fill="none" stroke="currentColor" stroke-width="2"><path d="M2 11v7h18v-7M11 2v10M7 8l4 4 4-4"/></svg>Download</div>
    <div class="action abs" style="left:1302px">
      <svg width="22" height="20" viewBox="0 0 22 20" fill="currentColor"><circle cx="4" cy="10" r="3"/><circle cx="17" cy="4" r="3"/><circle cx="17" cy="16" r="3"/><path d="M4 10L17 4M4 10l13 6" stroke="currentColor" stroke-width="2"/></svg>Share</div>
  </header>

  <h1 class="abs">Percentage of low-carbon power source in countries and regions, 1971 to 2018</h1>
  <p class="lead abs">Vestibulum malesuada nunc vitae turpis rhoncus suscipit. Nulla volutpat justo quis nulla vehicula hendrerit. Integer ultrices, ante et mollis fringilla, purus arcu finibus nisi, sit amet pretium nisl odio at mauris. Suspendisse consectetur vulputate tellus. Maecenas id dui purus. Morbi nec pellentesque velit, vel finibus felis. Nam sed diam ut risus maximus interdum. Suspendisse in facilisis velit. Lorem ipsum dolor sit amet, consectetur adipiscing elit.</p>

  <div class="select abs" style="left:55px;top:376px;width:193px">Search History <span>⌄</span></div>
  <div class="crumb abs" style="left:283px">Charts &nbsp; / <a>5 selected regions</a></div>
  <div class="toggle abs"></div>
  <div class="crumb abs" style="left:838px">Advanced View</div>
  <div class="select abs" style="left:984px;top:376px;width:193px">Region’s Progress <span>⌄</span></div>
  <div class="select abs" style="left:1192px;top:376px;width:193px">World <span>⌄</span></div>

  <div class="hint abs">Click on region’s name to view its full region details</div>

  <svg class="chart abs" width="1440" height="580" viewBox="0 520 1440 580">
    <g stroke="#e6e9ec" stroke-width="1">
      <line x1="110" x2="1294" y1="541" y2="541"/><line x1="110" x2="1294" y1="592" y2="592"/>
      <line x1="110" x2="1294" y1="643" y2="643"/><line x1="110" x2="1294" y1="694" y2="694"/>
      <line x1="110" x2="1294" y1="745" y2="745"/><line x1="110" x2="1294" y1="796" y2="796"/>
      <line x1="110" x2="1294" y1="847" y2="847"/><line x1="110" x2="1294" y1="898" y2="898"/>
      <line x1="110" x2="1294" y1="949" y2="949"/><line x1="110" x2="1294" y1="1000" y2="1000"/>
      <line x1="110" x2="1294" y1="1051" y2="1051" stroke="#c9ced4"/>
    </g>
    <g class="axis" text-anchor="end">
      <text x="94" y="547">100%</text><text x="94" y="598">90%</text><text x="94" y="649">80%</text>
      <text x="94" y="700">70%</text><text x="94" y="751">60%</text><text x="94" y="802">50%</text>
      <text x="94" y="853">40%</text><text x="94" y="904">30%</text><text x="94" y="955">20%</text>
      <text x="94" y="1006">10%</text><text x="94" y="1057">0%</text>
    </g>
    <g class="axis" text-anchor="middle">
      <text x="110" y="1086">1971</text><text x="211" y="1086">1975</text><text x="337" y="1086">1980</text>
      <text x="463" y="1086">1985</text><text x="589" y="1086">1990</text><text x="715" y="1086">1995</text>
      <text x="841" y="1086">2000</text><text x="967" y="1086">2005</text><text x="1093" y="1086">2010</text>
      <text x="1219" y="1086">2015</text><text x="1294" y="1086">2018</text>
    </g>
    <svg x="110" y="541" width="1184" height="510" viewBox="0 -100 47 100" preserveAspectRatio="none" overflow="visible" fill="none" stroke-linejoin="round">
      <g stroke="var(--brazil)">
        <polyline vector-effect="non-scaling-stroke" stroke-width="1.4" points="0,-85 1,-87 2,-88.5 3,-88.3 4,-87.3 5,-87.2 6,-86.2 7,-89 8,-90 9,-91.6 10,-91.2 11,-91.6 12,-92.5 13,-94.7 14,-92.9 15,-93.7 16,-94.6 17,-94.6 18,-97.6 19,-95.6 20,-96 21,-97 22,-95 23,-93.1 24,-92.4 25,-93.2 26,-93.5 27,-93.2 28,-91.6 29,-90.9 30,-90 31,-90.2 32,-90.2 33,-89.8 34,-91 35,-91.3 36,-90.8 37,-90 38,-90 39,-88.8 40,-88.8 41,-89 42,-86.3 43,-85.2 44,-86.3 45,-87.2 46,-87.5 47,-88"/>
        <path vector-effect="non-scaling-stroke" stroke-width="4.5" stroke-linecap="round" d="M0 -85h0M1 -87h0M2 -88.5h0M3 -88.3h0M4 -87.3h0M5 -87.2h0M6 -86.2h0M7 -89h0M8 -90h0M9 -91.6h0M10 -91.2h0M11 -91.6h0M12 -92.5h0M13 -94.7h0M14 -92.9h0M15 -93.7h0M16 -94.6h0M17 -94.6h0M18 -97.6h0M19 -95.6h0M20 -96h0M21 -97h0M22 -95h0M23 -93.1h0M24 -92.4h0M25 -93.2h0M26 -93.5h0M27 -93.2h0M28 -91.6h0M29 -90.9h0M30 -90h0M31 -90.2h0M32 -90.2h0M33 -89.8h0M34 -91h0M35 -91.3h0M36 -90.8h0M37 -90h0M38 -90h0M39 -88.8h0M40 -88.8h0M41 -89h0M42 -86.3h0M43 -85.2h0M44 -86.3h0M45 -87.2h0M46 -87.5h0M47 -88h0"/>
      </g>
      <g stroke="var(--us)">
        <polyline vector-effect="non-scaling-stroke" stroke-width="1.4" points="0,-42 1,-39.6 2,-38.3 3,-38.4 4,-39.5 5,-39.6 6,-40.6 7,-37.9 8,-36.9 9,-35.1 10,-35.5 11,-35.1 12,-34.1 13,-32 14,-33.8 15,-32.9 16,-32 17,-32 18,-29 19,-31 20,-30.5 21,-29.5 22,-31.5 23,-33.5 24,-34.5 25,-33.3 26,-33 27,-33.3 28,-35 29,-35.8 30,-36.8 31,-36.6 32,-36.6 33,-37 34,-35.7 35,-35.4 36,-35.9 37,-36.7 38,-36.7 39,-37.9 40,-37.9 41,-37.5 42,-40.5 43,-41.5 44,-40.4 45,-39.5 46,-39.2 47,-38.8"/>
        <path vector-effect="non-scaling-stroke" stroke-width="4.5" stroke-linecap="round" d="M0 -42h0M1 -39.6h0M2 -38.3h0M3 -38.4h0M4 -39.5h0M5 -39.6h0M6 -40.6h0M7 -37.9h0M8 -36.9h0M9 -35.1h0M10 -35.5h0M11 -35.1h0M12 -34.1h0M13 -32h0M14 -33.8h0M15 -32.9h0M16 -32h0M17 -32h0M18 -29h0M19 -31h0M20 -30.5h0M21 -29.5h0M22 -31.5h0M23 -33.5h0M24 -34.5h0M25 -33.3h0M26 -33h0M27 -33.3h0M28 -35h0M29 -35.8h0M30 -36.8h0M31 -36.6h0M32 -36.6h0M33 -37h0M34 -35.7h0M35 -35.4h0M36 -35.9h0M37 -36.7h0M38 -36.7h0M39 -37.9h0M40 -37.9h0M41 -37.5h0M42 -40.5h0M43 -41.5h0M44 -40.4h0M45 -39.5h0M46 -39.2h0M47 -38.8h0"/>
      </g>
      <g stroke="var(--uk)">
        <polyline vector-effect="non-scaling-stroke" stroke-width="1.4" points="0,-18.5 1,-21 2,-22.2 3,-22.1 4,-21 5,-20.9 6,-20 7,-22.6 8,-23.6 9,-25.4 10,-25 11,-25.3 12,-26.3 13,-28.5 14,-26.7 15,-27.5 16,-28.5 17,-28.5 18,-31.5 19,-29.5 20,-29.9 21,-30.8 22,-28.8 23,-26.9 24,-26 25,-27 26,-27.3 27,-27 28,-25.4 29,-24.8 30,-23.7 31,-24 32,-24 33,-23.5 34,-24.8 35,-25 36,-24.6 37,-23.7 38,-23.7 39,-22.6 40,-22.6 41,-22.8 42,-20 43,-19 44,-20 45,-21 46,-21.2 47,-21.6"/>
        <path vector-effect="non-scaling-stroke" stroke-width="4.5" stroke-linecap="round" d="M0 -18.5h0M1 -21h0M2 -22.2h0M3 -22.1h0M4 -21h0M5 -20.9h0M6 -20h0M7 -22.6h0M8 -23.6h0M9 -25.4h0M10 -25h0M11 -25.3h0M12 -26.3h0M13 -28.5h0M14 -26.7h0M15 -27.5h0M16 -28.5h0M17 -28.5h0M18 -31.5h0M19 -29.5h0M20 -29.9h0M21 -30.8h0M22 -28.8h0M23 -26.9h0M24 -26h0M25 -27h0M26 -27.3h0M27 -27h0M28 -25.4h0M29 -24.8h0M30 -23.7h0M31 -24h0M32 -24h0M33 -23.5h0M34 -24.8h0M35 -25h0M36 -24.6h0M37 -23.7h0M38 -23.7h0M39 -22.6h0M40 -22.6h0M41 -22.8h0M42 -20h0M43 -19h0M44 -20h0M45 -21h0M46 -21.2h0M47 -21.6h0"/>
      </g>
      <g stroke="var(--india)">
        <polyline vector-effect="non-scaling-stroke" stroke-width="1.4" points="0,-13 1,-12.6 2,-12.4 3,-11.4 4,-10.4 5,-11.5 6,-14.2 7,-14 8,-14 9,-15.2 10,-15.2 11,-15.9 12,-16.3 13,-16.1 14,-14.9 15,-15.3 16,-15.3 17,-15.1 18,-16 19,-16.7 20,-18.4 21,-18.5 22,-18.3 23,-17.4 24,-18.3 25,-20.2 26,-22.3 27,-21.3 28,-20.8 29,-22.9 30,-19.8 31,-19.8 32,-18.9 33,-18 34,-19.9 35,-17.6 36,-16.6 37,-16.3 38,-16.8 39,-15 40,-14 41,-11.4 42,-12.4 43,-12.4 44,-13.6 45,-13.6 46,-12.4 47,-10"/>
        <path vector-effect="non-scaling-stroke" stroke-width="4.5" stroke-linecap="round" d="M0 -13h0M1 -12.6h0M2 -12.4h0M3 -11.4h0M4 -10.4h0M5 -11.5h0M6 -14.2h0M7 -14h0M8 -14h0M9 -15.2h0M10 -15.2h0M11 -15.9h0M12 -16.3h0M13 -16.1h0M14 -14.9h0M15 -15.3h0M16 -15.3h0M17 -15.1h0M18 -16h0M19 -16.7h0M20 -18.4h0M21 -18.5h0M22 -18.3h0M23 -17.4h0M24 -18.3h0M25 -20.2h0M26 -22.3h0M27 -21.3h0M28 -20.8h0M29 -22.9h0M30 -19.8h0M31 -19.8h0M32 -18.9h0M33 -18h0M34 -19.9h0M35 -17.6h0M36 -16.6h0M37 -16.3h0M38 -16.8h0M39 -15h0M40 -14h0M41 -11.4h0M42 -12.4h0M43 -12.4h0M44 -13.6h0M45 -13.6h0M46 -12.4h0M47 -10h0"/>
      </g>
      <g stroke="var(--china)">
        <polyline vector-effect="non-scaling-stroke" stroke-width="1.4" points="0,-1.7 1,-4.1 2,-5.3 3,-5.2 4,-4.2 5,-4 6,-3.1 7,-5.7 8,-6.6 9,-8.4 10,-8 11,-8.5 12,-9.5 13,-11.6 14,-9.8 15,-10.6 16,-11.5 17,-11.5 18,-14.6 19,-12.6 20,-13.2 21,-14.1 22,-12.1 23,-10 24,-9.3 25,-10.2 26,-10.4 27,-10.2 28,-8.5 29,-7.7 30,-6.8 31,-7 32,-7 33,-6.7 34,-7.8 35,-8.2 36,-7.6 37,-6.8 38,-6.8 39,-5.7 40,-5.7 41,-5.9 42,-3 43,-2 44,-3.1 45,-4 46,-4.4 47,-4.8"/>
        <path vector-effect="non-scaling-stroke" stroke-width="4.5" stroke-linecap="round" d="M0 -1.7h0M1 -4.1h0M2 -5.3h0M3 -5.2h0M4 -4.2h0M5 -4h0M6 -3.1h0M7 -5.7h0M8 -6.6h0M9 -8.4h0M10 -8h0M11 -8.5h0M12 -9.5h0M13 -11.6h0M14 -9.8h0M15 -10.6h0M16 -11.5h0M17 -11.5h0M18 -14.6h0M19 -12.6h0M20 -13.2h0M21 -14.1h0M22 -12.1h0M23 -10h0M24 -9.3h0M25 -10.2h0M26 -10.4h0M27 -10.2h0M28 -8.5h0M29 -7.7h0M30 -6.8h0M31 -7h0M32 -7h0M33 -6.7h0M34 -7.8h0M35 -8.2h0M36 -7.6h0M37 -6.8h0M38 -6.8h0M39 -5.7h0M40 -5.7h0M41 -5.9h0M42 -3h0M43 -2h0M44 -3.1h0M45 -4h0M46 -4.4h0M47 -4.8h0"/>
      </g>
    </svg>
    <g class="series-label">
      <text x="1310" y="609" fill="var(--brazil)">Brazil</text>
      <text x="1310" y="859" fill="var(--us)">United</text><text x="1310" y="879" fill="var(--us)">States</text>
      <text x="1310" y="947" fill="var(--uk)">United</text><text x="1310" y="967" fill="var(--uk)">Kingdom</text>
      <text x="1310" y="1006" fill="var(--india)">India</text>
      <text x="1310" y="1033" fill="var(--china)">China</text>
    </g>
  </svg>

  <h2 class="energy abs">Energy Sources</h2>
  <div class="energy-note abs">Select an energy source to view its data</div>

  <section class="src-panel abs" style="left:55px;width:658px">
    <div class="opt" style="left:45px;top:34px"><span class="radio on"></span><span class="sw" style="background:#5ee8c0"></span>Nonfossil</div>
    <div class="opt" style="left:82px;top:83px"><span class="radio"></span><span class="sw" style="background:#14c3b8"></span>Hydro</div>
    <div class="opt" style="left:82px;top:122px"><span class="radio"></span><span class="sw" style="background:#1b95b0"></span>Nuclear</div>
    <div class="opt" style="left:82px;top:161px"><span class="radio"></span><span class="sw" style="background:#7dd87a"></span>Renewables-except-hydro</div>
    <div class="opt" style="left:379px;top:83px"><span class="radio"></span><span class="sw" style="background:#f5f07a"></span>Solar</div>
    <div class="opt" style="left:379px;top:122px"><span class="radio"></span><span class="sw" style="background:#eef0e2"></span>Wind</div>
    <div class="opt" style="left:379px;top:161px"><span class="radio"></span><span class="sw" style="background:#f2bf3a"></span>Other-renewables</div>
  </section>
  <section class="src-panel abs" style="left:728px;width:657px">
    <div class="opt" style="left:45px;top:35px"><span class="radio"></span><span class="sw" style="background:#f2295f"></span>Fossil</div>
    <div class="opt" style="left:82px;top:83px"><span class="radio"></span><span class="sw" style="background:#8a1a3a"></span>Coal</div>
    <div class="opt" style="left:82px;top:122px"><span class="radio"></span><span class="sw" style="background:#c81f5a"></span>Oil</div>
    <div class="opt" style="left:82px;top:161px"><span class="radio"></span><span class="sw" style="background:#9c6270"></span>Gas</div>
    <div class="opt" style="left:379px;top:83px"><span class="radio"></span><span class="sw" style="background:#f48fb3"></span>Unspecified-fossil-fuels</div>
    <div class="opt" style="left:379px;top:122px"><span class="radio"></span><span class="sw" style="background:#fbdbe6"></span>Other</div>
  </section>

  <section class="regions abs">
    <h3>5 selected countries and regions</h3>
    <div class="opt" style="left:599px;top:46px"><span class="box"></span>Select all</div>
    <div class="opt" style="left:725px;top:46px"><svg width="22" height="22" viewBox="0 0 22 22" style="margin-right:14px"><path d="M3 3l16 16M19 3L3 19" stroke="var(--ink)" stroke-width="3"/></svg>Unselect all</div>
    <div class="search">Search regions
      <svg width="18" height="18" viewBox="0 0 18 18" style="position:absolute;right:14px;top:8px" fill="none" stroke="var(--ink)" stroke-width="2"><circle cx="7.5" cy="7.5" r="5.5"/><path d="M11.5 11.5L16 16"/></svg></div>
    <div class="grid">
      <div class="cell" style="left:0;top:0"><span class="box on"><svg width="16" height="12" viewBox="0 0 16 12"><path d="M2 6l4 4 8-8" stroke="#fff" stroke-width="2.5" fill="none"/></svg></span>United States</div>
      <div class="cell" style="left:0;top:36px"><span class="box on"><svg width="16" height="12" viewBox="0 0 16 12"><path d="M2 6l4 4 8-8" stroke="#fff" stroke-width="2.5" fill="none"/></svg></span>United Kingdom</div>
      <div class="cell" style="left:0;top:72px"><span class="box on"><svg width="16" height="12" viewBox="0 0 16 12"><path d="M2 6l4 4 8-8" stroke="#fff" stroke-width="2.5" fill="none"/></svg></span>China</div>
      <div class="cell" style="left:0;top:108px"><span class="box on"><svg width="16" height="12" viewBox="0 0 16 12"><path d="M2 6l4 4 8-8" stroke="#fff" stroke-width="2.5" fill="none"/></svg></span>India</div>
      <div class="cell" style="left:0;top:144px"><span class="box on"><svg width="16" height="12" viewBox="0 0 16 12"><path d="M2 6l4 4 8-8" stroke="#fff" stroke-width="2.5" fill="none"/></svg></span>Brazil</div>
      <div class="cell" style="left:0;top:180px"><span class="box"></span>Antigua and Barbuda</div>
      <div class="cell" style="left:0;top:216px"><span class="box"></span>Argentina</div>

      <div class="cell" style="left:259px;top:0"><span class="box"></span>Afghanistan</div>
      <div class="cell" style="left:259px;top:36px"><span class="box"></span>Albania</div>
      <div class="cell" style="left:259px;top:72px"><span class="box"></span>Algeria</div>
      <div class="cell" style="left:259px;top:108px"><span class="box"></span>Andorra</div>
      <div class="cell" style="left:259px;top:144px"><span class="box"></span>Angola</div>
      <div class="cell" style="left:259px;top:180px"><span class="box"></span>Antigua and Barbuda</div>
      <div class="cell" style="left:259px;top:216px"><span class="box"></span>Argentina</div>

      <div class="cell" style="left:518px;top:0"><span class="box"></span>Afghanistan</div>
      <div class="cell" style="left:518px;top:36px"><span class="box"></span>Albania</div>
      <div class="cell" style="left:518px;top:72px"><span class="box"></span>Algeria</div>
      <div class="cell" style="left:518px;top:108px"><span class="box"></span>Andorra</div>
      <div class="cell" style="left:518px;top:144px"><span class="box"></span>Angola</div>
      <div class="cell" style="left:518px;top:180px"><span class="box"></span>Antigua and Barbuda</div>
      <div class="cell" style="left:518px;top:216px"><span class="box"></span>Argentina</div>

      <div class="cell" style="left:777px;top:0"><span class="box"></span>Afghanistan</div>
      <div class="cell" style="left:777px;top:36px"><span class="box"></span>Albania</div>
      <div class="cell" style="left:777px;top:72px"><span class="box"></span>Algeria</div>
      <div class="cell" style="left:777px;top:108px"><span class="box"></span>Andorra</div>
      <div class="cell" style="left:777px;top:144px"><span class="box"></span>Angola</div>
      <div class="cell" style="left:777px;top:180px"><span class="box"></span>Antigua and Barbuda</div>
      <div class="cell" style="left:777px;top:216px"><span class="box"></span>Argentina</div>

      <div class="cell" style="left:1017px;top:0"><span class="box"></span>Afghanistan</div>
      <div class="cell" style="left:1017px;top:36px"><span class="box"></span>Albania</div>
      <div class="cell" style="left:1017px;top:72px"><span class="box"></span>Algeria</div>
      <div class="cell" style="left:1017px;top:108px"><span class="box"></span>Andorra</div>
      <div class="cell" style="left:1017px;top:144px"><span class="box"></span>Angola</div>
      <div class="cell" style="left:1017px;top:180px"><span class="box"></span>Antigua and Barbuda</div>
      <div class="cell" style="left:1017px;top:216px"><span class="box"></span>Argentina</div>
    </div>
    <div class="scroll"><i></i></div>
  </section>

  <h2 class="concl abs">The most important general conclusions that can be drawn from the data</h2>
  <p class="concl-lead abs">Lorem ipsum dolor sit amet, consectetur adipiscing elit. Aliquam et nibh porta ante pretium finibus. Vivamus ultricies quam eu orci gravida, vel fermentum orci tincidunt. In egestas pharetra sem id sodales. Pellentesque tristique pulvinar urna, in tristique magna mollis ac. Etiam eget ex hendrerit velit blandit porta. Phasellus sed interdum nisl.</p>

  <ul class="points abs" style="left:55px;top:2060px;width:660px">
    <li>The world as a whole is NOT moving away from fossil fuels for electricity generation.</li>
    <li>There are substantial differences between energy sources. Regions that have successfully decarbonized their electricity generation have usually done so using hydro and/or nuclear. Other low-carbon energy sources have grown quickly in relative terms in the last few years but are so far contributing little in absolute numbers.</li>
  </ul>
  <ul class="points abs" style="left:734px;top:2060px;width:640px">
    <li>There are substantial differences between regions.
      <ul>
        <li>Some regions have basically solved the problem – they already generate almost all of their electricity from non-fossil sources.</li>
        <li>Some regions have greatly improved in terms of decarbonizing their electricity generation.</li>
        <li>Some regions have greatly deteriorated, in other words they are using a much higher share of fossil fuels to generate their electricity.</li>
      </ul>
    </li>
  </ul>

  <div class="footer abs" style="left:55px;font-weight:400">Data source: &nbsp;<a href="#" style="text-decoration:underline">Tessaro Fund</a> , &nbsp;<a href="#" style="text-decoration:underline">KQ</a></div>
  <div class="footer abs" style="right:55px">For any questions please feel free to email me at <a class="mail" href="#" style="text-decoration:underline">o@voltmeadow.net</a></div>
</div>
</body>
</html>
```